Brennick & Vale, LLC
Law firm stationary and business cards
Brennick & Vale, LLC -
Creative Brief
Professional
Miles R. Dorsey
2875 Oakridge Avenue, Suite 410 Kansas City, Missouri 64187
miles@brennickvale-law.example
www.brennickvale-law.example

```html
<!DOCTYPE html>
<html lang="en">
<head>
<meta charset="utf-8">
<title>Brennick &amp; Vale, LLC — Stationery</title>
<link rel="stylesheet" href="https://fonts.googleapis.com/css2?family=Libre+Baskerville:wght@400;700&family=Open+Sans:wght@400;600&display=swap">
<style>
:root{
  --bg:#e9e9ea;
  --paper:#ffffff;
  --navy:#1f4e9c;
  --navy-dark:#173d7d;
  --ink:#2c3a4f;
  --muted:#8a93a0;
  --faint:#e6eaf1;
  --panel-top:#6b6c6e;
  --panel-bottom:#3e3f41;
}
*{margin:0;padding:0;box-sizing:border-box}
html,body{width:1200px;height:346px;overflow:hidden;background:var(--bg)}
body{position:relative;font-family:"Open Sans",Arial,sans-serif;color:var(--ink)}
.piece{position:absolute;background:var(--paper);box-shadow:0 1px 3px rgba(0,0,0,.25);overflow:hidden}
.label{position:absolute;font-size:5px;color:var(--muted);text-align:center}
.brand{display:flex;align-items:center;gap:3px;font-family:"Libre Baskerville",Georgia,serif;font-weight:700;color:var(--navy);white-space:nowrap}
.brand .mark{background:var(--navy);flex:none}
.brand-sm{font-size:5px}.brand-sm .mark{width:7px;height:7px}
.brand-md{font-size:8px}.brand-md .mark{width:11px;height:11px}
.band{position:absolute;left:0;right:0;bottom:0;background:var(--navy)}
.faint-square{position:absolute;background:var(--faint)}
.tiny{font-size:3.6px;line-height:1.5;color:var(--ink)}

.showcase-brand{position:absolute;left:19px;top:70px}
.showcase-note{position:absolute;left:19px;top:93px;font-size:5px;color:var(--muted)}

.card-front{left:19px;top:140px;width:125px;height:82px}
.card-front .brand{position:absolute;left:8px;top:8px}
.card-front .person{position:absolute;left:8px;top:30px}
.card-front .name{font-family:"Libre Baskerville",Georgia,serif;font-size:5.5px;color:var(--navy);font-weight:700}
.card-front .band{height:4px}
.card-back{left:19px;top:238px;width:125px;height:72px}
.card-back .brand{position:absolute;left:8px;top:10px}
.card-back .details{position:absolute;left:8px;top:30px}
.card-back .band{height:4px}

.letterhead{top:17px;width:228px;height:288px}
.letterhead.p1{left:158px}.letterhead.p2{left:400px}
.letterhead .brand{position:absolute;left:14px;top:14px}
.letterhead .contact{position:absolute;right:14px;top:14px;text-align:left;width:80px}
.letterhead .faint-square{left:74px;top:104px;width:80px;height:80px}
.letterhead .footer{position:absolute;left:0;right:0;bottom:9px;text-align:center;font-size:3.6px;color:var(--muted)}
.letterhead .band{height:5px}

.envelope{left:643px;width:233px}
.envelope.front{top:149px;height:72px}
.envelope.window{top:247px;height:52px}
.envelope .brand{position:absolute;left:8px;top:7px}
.envelope .return{position:absolute;left:8px;top:20px}
.envelope .faint-square{left:96px;top:10px;width:46px;height:46px}
.envelope .addr-window{position:absolute;left:30px;top:28px;width:80px;height:16px;border:0.6px solid #d5d9e0;border-radius:2px}
.envelope .band{height:3px}

.backs-panel{position:absolute;left:900px;top:0;width:300px;height:346px;background:linear-gradient(180deg,var(--panel-top),var(--panel-bottom))}
.env-back{position:absolute;left:20px;width:270px;box-shadow:0 2px 4px rgba(0,0,0,.4)}
.env-back svg{display:block}
.env-back.white-top{top:89px;height:60px}
.env-back.blue{top:150px;height:70px}
.env-back.white-bottom{top:228px;height:72px}
.env-back .flap-brand{position:absolute;left:50%;transform:translateX(-50%);top:24px;color:#fff}
.env-back .flap-brand .mark{background:#fff}
</style>
</head>
<body>

<div class="showcase-brand brand brand-md"><span class="mark"></span>BRENNICK &amp; VALE, LLC</div>
<div class="showcase-note">Stationery &amp; Designs</div>

<section class="piece card-front" aria-label="Business card front">
  <div class="brand brand-sm"><span class="mark"></span>BRENNICK &amp; VALE, LLC</div>
  <div class="person tiny">
    <div class="name">Miles R. Dorsey</div>
    <div>Attorney at Law</div>
    <div>(816) 555-0142</div>
    <div>miles@brennickvale-law.example</div>
  </div>
  <div class="band"></div>
</section>
<div class="label" style="left:19px;top:226px;width:125px">Business Card Front</div>

<section class="piece card-back" aria-label="Business card back">
  <div class="brand brand-sm"><span class="mark"></span>BRENNICK &amp; VALE, LLC</div>
  <div class="details tiny">
    <div>2875 Oakridge Avenue, Suite 410</div>
    <div>Kansas City, Missouri 64187</div>
    <div>www.brennickvale-law.example</div>
  </div>
  <div class="band"></div>
</section>
<div class="label" style="left:19px;top:314px;width:125px">Business Card Back</div>

<section class="piece letterhead p1" aria-label="Letterhead first page">
  <div class="brand brand-sm"><span class="mark"></span>BRENNICK &amp; VALE, LLC</div>
  <div class="contact tiny">
    <div>2875 Oakridge Avenue, Suite 410</div>
    <div>Kansas City, Missouri 64187</div>
    <div>P (816) 555-0142 · F (816) 555-0143</div>
  </div>
  <div class="faint-square"></div>
  <div class="footer">www.brennickvale-law.example</div>
  <div class="band"></div>
</section>
<div class="label" style="left:158px;top:309px;width:228px">Letterhead Page 1</div>

<section class="piece letterhead p2" aria-label="Letterhead second page">
  <div class="faint-square"></div>
  <div class="band"></div>
</section>
<div class="label" style="left:400px;top:309px;width:228px">Letterhead Page 2</div>

<section class="piece envelope front" aria-label="Envelope front">
  <div class="faint-square"></div>
  <div class="brand brand-sm"><span class="mark"></span>BRENNICK &amp; VALE, LLC</div>
  <div class="return tiny">
    <div>2875 Oakridge Avenue, Suite 410</div>
    <div>Kansas City, Missouri 64187</div>
  </div>
  <div class="band"></div>
</section>
<div class="label" style="left:643px;top:225px;width:233px">Envelope Front</div>

<section class="piece envelope window" aria-label="Window envelope front">
  <div class="brand brand-sm"><span class="mark"></span>BRENNICK &amp; VALE, LLC</div>
  <div class="addr-window"></div>
  <div class="band"></div>
</section>
<div class="label" style="left:643px;top:303px;width:233px">Envelope Window</div>

<div class="backs-panel">
  <div class="env-back white-top">
    <svg width="270" height="60" viewBox="0 0 270 60">
      <rect width="270" height="60" fill="#f4f4f5"/>
      <path d="M0 0 L135 34 L270 0 Z" fill="#ffffff" stroke="#d3d5d9" stroke-width="0.6"/>
      <path d="M0 60 L110 30 M270 60 L160 30" stroke="#dcdde0" stroke-width="0.6"/>
    </svg>
  </div>
  <div class="env-back blue">
    <svg width="270" height="70" viewBox="0 0 270 70">
      <rect width="270" height="70" fill="#f4f4f5"/>
      <path d="M0 0 L270 0 L270 18 L135 56 L0 18 Z" fill="var(--navy)"/>
    </svg>
    <div class="flap-brand brand brand-sm"><span class="mark"></span></div>
  </div>
  <div class="env-back white-bottom">
    <svg width="270" height="72" viewBox="0 0 270 72">
      <rect width="270" height="72" fill="#f7f7f8"/>
      <path d="M0 0 L135 40 L270 0" fill="none" stroke="#cfd2d7" stroke-width="0.7"/>
      <path d="M0 72 L112 34 M270 72 L158 34" stroke="#dcdde0" stroke-width="0.6"/>
    </svg>
    <div class="brand brand-sm" style="position:absolute;left:129px;top:10px"><span class="mark"></span></div>
  </div>
</div>

</body>
</html>
```